依頼詳細
PCとスマホデザインの両方納品をいただきますが、
まずはデザインイメージが確認しやすいPCページのみの提案をお願いします。
スマホページは当選者に納品時にお願いしたいと思います。
スマホサイズについて、カンバスサイズは横幅375pxで作成し、2倍の横幅750pxのサイズで書き出ししてください。
(Retinaディスプレイに対応するため)
スマホページ作成時は、メニューが展開した際のデザインもお願いします。
レスポンシブウェブデザインを意識したデザインでお願いします。

■サイトマップ
添付の画面遷移図をご確認ください。

■参考サイト
https://harbor-mend-crew.com/
https://www.qv-tm.co.jp/

■内容について
工場や倉庫の修繕・改修・増築などを専門とするサービスサイトになります。

■素材写真
画像データについては、フリー素材から流用して
イメージ画像に当て込んでください。
足りない場合は、一旦他のサイトの写真をサンプルとして
入れてください。(サンプルなどの表記をお願いします)
また、購入が必要な写真などを利用した場合、
価格とサイト名を教えてください。

また、Nimbrel Stockで定期契約をしていますので、
Nimbrel Stockの画像は使用できます。
デザイン時はカンプ画像をお入れいただきますようお願いします。

■ロゴについて
添付のロゴデータを使用してください。

■ワイヤーフレーム
https://mk.velquora.com/view/600e5e1a-e3bd-4b32-a74b-244a4501d661-355d/?fullscreen
コンテンツの構成としてワイヤーフレームを作成しましたが
必ずしもワイヤーフレームの通りではなくて大丈夫です。
TOPページに配置するコンテンツを見ていただき、デザインは
デザイナーの皆様におまかせしたいと思います。

----------------------------------------------------------------------------
【制作物に対するお願い】

■フォントについて
・無料で使えるフォントで作成をお願いします。
・OSに紐づくフォントの使用は控えていただければと思います (ヒラギノなど)

サイトURL
ページ数
1ページ
希望イメージ
シンプル 複雑
単色 カラフル
暗い 明るい
日常 高級
遊び心 厳粛
未来的 伝統的
女性的 男性的
希望する色
ベースカラー:白、ポイントカラー:赤、青(救急のイメージ)
納品ファイル
• 高解像度JPG (.jpg)
• イラストレーター形式 (.ai)
• フォトショップ形式 (.psd)
補足説明
上記のいずれか1つ(アウトラインありとなしの2つ)と高解像度JPGを納品お願いします。
adobe XDでの納品も可能です。

```html
<!DOCTYPE html>
<html lang="ja">
<head>
<meta charset="utf-8">
<title>工場リペアナビ | 工場専門修繕サービス</title>
<link rel="stylesheet" href="https://fonts.googleapis.com/css2?family=Noto+Sans+JP:wght@400;500;700;900&family=Oswald:wght@500;600&display=swap">
<style>
:root{
  --red:#e3202c;
  --blue:#175fc1;
  --ink:#1a1a1a;
  --sub:#555;
  --line:#d9d9d9;
  --gray:#f1f1f1;
  --white:#fff;
  --navy:#1e3d7a;
}
*{box-sizing:border-box;margin:0;padding:0}
html,body{width:1200px;height:4148px;overflow:hidden}
body{font-family:"Noto Sans JP",sans-serif;color:var(--ink);background:var(--white);position:relative;font-size:13px}
a{color:inherit;text-decoration:none}
.abs{position:absolute}
.photo{position:absolute}

/* header */
.header{position:absolute;left:0;top:0;width:1200px;height:100px;background:var(--white);z-index:5}
.brand{position:absolute;left:20px;top:26px;display:flex;align-items:center;gap:10px}
.brand-mark{width:34px;height:34px;background:var(--blue);border-radius:4px}
.brand-name{font-size:30px;font-weight:900;color:var(--blue);letter-spacing:1px}
.subnav{position:absolute;left:370px;top:24px;display:flex;gap:26px;font-size:13px;font-weight:500}
.mainnav{position:absolute;left:370px;top:66px;display:flex;gap:40px;font-size:13px;font-weight:500}
.tel{position:absolute;left:586px;top:14px;display:flex;align-items:center;gap:8px;font-family:"Oswald",sans-serif;font-size:30px;font-weight:600}
.hbtn{position:absolute;top:22px;height:32px;color:#fff;font-size:12px;font-weight:700;display:flex;align-items:center;justify-content:center}
.hbtn.blue{left:800px;width:196px;background:var(--blue)}
.hbtn.red{left:1006px;width:176px;background:var(--red)}
.dropdown{position:absolute;left:564px;top:100px;width:170px;background:#fff;border:1px solid var(--line);z-index:6}
.dropdown li{list-style:none;height:66px;display:flex;align-items:center;justify-content:center;border-bottom:1px solid var(--line);font-size:13px;font-weight:500}
.dropdown li:first-child{background:#eef2fa}

/* hero */
.hero{left:0;top:100px;width:1200px;height:600px;background:linear-gradient(120deg,#1a2430 0%,#3a4a58 40%,#8a8f94 70%,#2c3742 100%)}
.scroll{position:absolute;left:14px;top:640px;writing-mode:vertical-rl;font-family:"Oswald",sans-serif;font-size:11px;letter-spacing:3px;color:#fff;z-index:2}

/* section titles */
.ttl{position:absolute}
.ttl h2{font-size:26px;font-weight:900;line-height:1.2}
.ttl p{font-family:"Oswald",sans-serif;font-size:14px;font-weight:600;letter-spacing:2px;margin-top:4px}
.ttl p span{color:var(--red)}
.ttl::before{content:"";position:absolute;left:0;top:-12px;width:36px;height:3px;background:var(--blue)}

.btn{position:absolute;height:44px;color:#fff;font-size:13px;font-weight:700;display:flex;align-items:center;justify-content:center;gap:20px}
.btn.blue{background:var(--blue)}
.btn.red{background:var(--red)}
.btn svg{width:18px;height:12px}

/* feature */
.feature-bg{left:0;top:700px;width:1200px;height:1060px;background:var(--gray)}
.feature-photo{left:0;top:700px;width:440px;height:460px;background:linear-gradient(135deg,#0e2030,#2d5a7a 50%,#8aa8bc)}
.feature-text{position:absolute;left:472px;top:856px;width:680px;font-size:12px;line-height:2;color:var(--sub)}
.feature-text p+p{margin-top:18px}

/* works */
.card-panel{position:absolute;left:140px;top:1220px;width:920px;height:460px;background:#fff;box-shadow:0 2px 10px rgba(0,0,0,.08)}
.work{position:absolute;top:1348px;width:240px}
.work .photo{position:relative;height:150px;background:linear-gradient(180deg,#0b2a58,#2f7bc6 60%,#bcd6ee)}
.work-meta{text-align:center;font-size:12px;line-height:1.7;margin:12px 0 12px}
.work .btn{position:relative;width:240px;height:40px}

/* column */
.col-main{position:absolute;left:192px;top:1850px;width:450px;height:530px;background:#fff;box-shadow:0 2px 12px rgba(0,0,0,.1)}
.col-side{position:absolute;left:740px;width:300px;height:250px;background:#fff;box-shadow:0 2px 12px rgba(0,0,0,.1)}
.colimg{background:linear-gradient(180deg,#7a9cc2,#cfdde8 55%,#4d5e72)}
.date{font-size:11px;color:var(--sub)}
.ctitle{font-weight:700;line-height:1.8}
.cexc{font-size:11px;color:var(--sub);line-height:1.8}
.circle-arrow{position:absolute;width:32px;height:32px;border:1px solid #333;border-radius:50%;display:flex;align-items:center;justify-content:center}

/* news */
.news-list{position:absolute;left:460px;top:2530px;width:700px}
.news-item{display:flex;align-items:center;height:80px;border-bottom:1px solid var(--line)}
.news-date{width:90px;display:flex;align-items:center;gap:6px}
.news-date b{font-family:"Oswald",sans-serif;font-size:30px}
.news-date small{font-family:"Oswald",sans-serif;font-size:9px;line-height:1.3}
.news-text{flex:1;font-size:11px;line-height:1.8;color:var(--sub)}

/* contents */
.contents-bg{left:0;top:2800px;width:1200px;height:500px;background:var(--gray)}
.contents-photo{left:688px;top:2860px;width:512px;height:420px;background:linear-gradient(135deg,#3c2a1c,#a87a52 45%,#e0c9a8 80%,#6b5a48)}
.clinks{position:absolute;left:192px;top:2970px;width:420px;list-style:none}
.clinks li{height:64px;border-bottom:1px solid #999;display:flex;align-items:center;justify-content:space-between;font-weight:700;font-size:14px}

/* contact */
.contact-lead{position:absolute;left:192px;top:3470px;font-size:12px;line-height:2;color:var(--sub)}
.pill{position:absolute;left:620px;width:420px;height:96px;border:1px solid #bbb;border-radius:48px;background:#fff;display:flex;align-items:center;gap:18px;padding-left:28px}
.pill .icon{width:48px;height:48px;border-radius:50%;display:flex;align-items:center;justify-content:center}
.pill-tel small{display:block;font-size:10px;line-height:1.5}
.pill-tel b{font-family:"Oswald",sans-serif;font-size:30px;color:var(--red);line-height:1.1}

/* footer */
.footer{left:0;top:3680px;width:1200px;height:468px;background:#f5f5f5}
.flinks{position:absolute;top:3730px;list-style:none;font-size:12px;line-height:1}
.flinks li{margin-bottom:22px}
.copy{position:absolute;left:0;top:4100px;width:1200px;text-align:center;font-size:10px;color:var(--sub)}
</style>
</head>
<body>

<header class="header">
  <a class="brand" href="#"><span class="brand-mark"></span><span class="brand-name">工場リペアナビ</span></a>
  <nav class="subnav"><a>会社概要</a><a>よくあるご質問</a></nav>
  <nav class="mainnav"><a>ホーム</a><a>工場リペアナビの特徴</a><a>サービス一覧</a><a>施工実績</a><a>お問い合わせ</a></nav>
  <div class="tel">
    <svg width="24" height="24" viewBox="0 0 24 24"><circle cx="12" cy="12" r="12" fill="#e3202c"/><path d="M8 6l2.5 3-1.5 1.5c.8 1.8 2.2 3.2 4 4l1.5-1.5 3 2.5-1.5 2.5c-5 0-10-5-10-10z" fill="#fff"/></svg>
    0120-48-3917
  </div>
  <a class="hbtn blue">カタログダウンロード</a>
  <a class="hbtn red">無料お見積り</a>
</header>
<ul class="dropdown">
  <li>屋根・防水</li><li>電設</li><li>設備</li><li>内装工事</li><li>解体工事</li><li>省エネ・コスト削減</li>
</ul>

<div class="photo hero" role="img" aria-label="工場内のロボットアームとタブレットを操作する作業員の写真"></div>

<div class="photo feature-bg"></div>
<div class="photo feature-photo" role="img" aria-label="制御モニターを確認する技術者の写真"></div>
<div class="scroll">SCROLL</div>
<div class="ttl" style="left:472px;top:762px"><h2>工場専門修繕サービス</h2><p><span>F</span>EATURE</p></div>
<div class="feature-text">
  <p>テキストが入ります。テキストが入ります。テキストが入ります。テキストが入ります。テキストが入ります。テキストが入ります。テキストが入ります。テキストが入ります。テキストが入ります。テキストが入ります。テキストが入ります。テキストが入ります。テキストが入ります。</p>
  <p>テキストが入ります。テキストが入ります。テキストが入ります。テキストが入ります。テキストが入ります。テキストが入ります。テキストが入ります。テキストが入ります。テキストが入ります。</p>
  <p>テキストが入ります。テキストが入ります。テキストが入ります。テキストが入ります。テキストが入ります。テキストが入ります。テキストが入ります。テキストが入ります。テキストが入ります。テキストが入ります。テキストが入ります。テキストが入ります。</p>
</div>
<a class="btn blue" style="left:472px;top:1110px;width:240px">詳しくみる<svg viewBox="0 0 18 12"><path d="M0 6h16M11 1l5 5-5 5" stroke="#fff" stroke-width="2" fill="none"/></svg></a>

<div class="card-panel"></div>
<div class="ttl" style="left:192px;top:1262px"><h2>施工実績</h2><p><span>W</span>ORKS</p></div>
<a class="btn red" style="left:776px;top:1262px;width:232px">施工実績一覧<svg viewBox="0 0 18 12"><path d="M0 6h16M11 1l5 5-5 5" stroke="#fff" stroke-width="2" fill="none"/></svg></a>
<div class="work" style="left:192px"><div class="photo" role="img" aria-label="倉庫内の施工実績写真"></div><p class="work-meta">株式会社●●●●<br>工場修繕工事</p><a class="btn blue">詳しくみる<svg viewBox="0 0 18 12"><path d="M0 6h16M11 1l5 5-5 5" stroke="#fff" stroke-width="2" fill="none"/></svg></a></div>
<div class="work" style="left:482px"><div class="photo" role="img" aria-label="倉庫内の施工実績写真"></div><p class="work-meta">株式会社●●●●<br>工場修繕工事</p><a class="btn blue">詳しくみる<svg viewBox="0 0 18 12"><path d="M0 6h16M11 1l5 5-5 5" stroke="#fff" stroke-width="2" fill="none"/></svg></a></div>
<div class="work" style="left:772px"><div class="photo" role="img" aria-label="倉庫内の施工実績写真"></div><p class="work-meta">株式会社●●●●<br>工場修繕工事</p><a class="btn blue">詳しくみる<svg viewBox="0 0 18 12"><path d="M0 6h16M11 1l5 5-5 5" stroke="#fff" stroke-width="2" fill="none"/></svg></a></div>

<div class="ttl" style="left:192px;top:1766px"><h2>コラム</h2><p><span>C</span>OLUMU</p></div>
<a class="btn red" style="left:776px;top:1766px;width:232px">コラム一覧<svg viewBox="0 0 18 12"><path d="M0 6h16M11 1l5 5-5 5" stroke="#fff" stroke-width="2" fill="none"/></svg></a>
<article class="col-main">
  <div class="photo colimg" style="left:20px;top:20px;width:410px;height:240px" role="img" aria-label="近代的な倉庫建築の写真"></div>
  <p class="date abs" style="left:20px;top:278px">2021.11.01</p>
  <p class="ctitle abs" style="left:20px;top:306px;width:410px;font-size:15px">タイトルがはいりますタイトルがはいりますタイトルがはいりますタイトルがはいります</p>
  <p class="cexc abs" style="left:20px;top:376px;width:410px">記事の冒頭の文章の一部が表示されます記事の冒頭の文章の一部が表示されます記事の冒頭の文章の一部が表示されます記事</p>
  <span class="circle-arrow" style="left:398px;top:478px"><svg width="14" height="10" viewBox="0 0 14 10"><path d="M0 5h12M8 1l4 4-4 4" stroke="#333" stroke-width="1.5" fill="none"/></svg></span>
</article>
<article class="col-side" style="top:1850px">
  <div class="photo colimg" style="left:16px;top:16px;width:268px;height:130px" role="img" aria-label="近代的な倉庫建築の写真"></div>
  <p class="date abs" style="left:16px;top:156px">2021.11.01</p>
  <p class="ctitle abs" style="left:16px;top:174px;width:268px;font-size:11px">タイトルがはいりますタイトルがはいりますタイトルがはいります</p>
  <span class="circle-arrow" style="left:252px;top:212px;width:28px;height:28px"><svg width="12" height="10" viewBox="0 0 14 10"><path d="M0 5h12M8 1l4 4-4 4" stroke="#333" stroke-width="1.5" fill="none"/></svg></span>
</article>
<article class="col-side" style="top:2126px">
  <div class="photo colimg" style="left:16px;top:16px;width:268px;height:130px" role="img" aria-label="近代的な倉庫建築の写真"></div>
  <p class="date abs" style="left:16px;top:156px">2021.11.01</p>
  <p class="ctitle abs" style="left:16px;top:174px;width:268px;font-size:11px">タイトルがはいりますタイトルがはいりますタイトルがはいります</p>
  <span class="circle-arrow" style="left:252px;top:212px;width:28px;height:28px"><svg width="12" height="10" viewBox="0 0 14 10"><path d="M0 5h12M8 1l4 4-4 4" stroke="#333" stroke-width="1.5" fill="none"/></svg></span>
</article>

<div class="ttl" style="left:192px;top:2460px"><h2>お知らせ</h2><p><span>N</span>EWS</p></div>
<a class="btn red" style="left:192px;top:2534px;width:240px">お知らせ一覧<svg viewBox="0 0 18 12"><path d="M0 6h16M11 1l5 5-5 5" stroke="#fff" stroke-width="2" fill="none"/></svg></a>
<div class="news-list">
  <div class="news-item"><div class="news-date"><b>13</b><small>2021<br>NOV</small></div><p class="news-text">テキストが入ります。テキストが入ります。テキストが入ります。テキストが入ります。<br>テキストが入ります。テキストが入ります。テキストが入ります。</p></div>
  <div class="news-item"><div class="news-date"><b>12</b><small>2021<br>NOV</small></div><p class="news-text">テキストが入ります。テキストが入ります。テキストが入ります。テキストが入ります。<br>テキストが入ります。テキストが入ります。テキストが入ります。</p></div>
  <div class="news-item"><div class="news-date"><b>01</b><small>2021<br>NOV</small></div><p class="news-text">テキストが入ります。テキストが入ります。テキストが入ります。テキストが入ります。<br>テキストが入ります。テキストが入ります。テキストが入ります。</p></div>
</div>

<div class="photo contents-bg"></div>
<div class="photo contents-photo" role="img" aria-label="図面と建築模型を確認する手元の写真"></div>
<div class="ttl" style="left:192px;top:2860px"><h2>コンテンツ</h2><p><span>C</span>ONTENTS</p></div>
<ul class="clinks">
  <li>よくあるご質問<svg width="18" height="12" viewBox="0 0 18 12"><path d="M0 6h16M11 1l5 5-5 5" stroke="#333" stroke-width="1.5" fill="none"/></svg></li>
  <li>お打ちかわせの流れ<svg width="18" height="12" viewBox="0 0 18 12"><path d="M0 6h16M11 1l5 5-5 5" stroke="#333" stroke-width="1.5" fill="none"/></svg></li>
  <li>カタログダウンロード<svg width="18" height="12" viewBox="0 0 18 12"><path d="M0 6h16M11 1l5 5-5 5" stroke="#333" stroke-width="1.5" fill="none"/></svg></li>
</ul>

<div class="ttl" style="left:192px;top:3396px"><h2>お問い合わせ</h2><p><span>C</span>ONTACT</p></div>
<p class="contact-lead">ご相談やご質問など、<br>お気軽にお問い合わせください。</p>
<div class="pill" style="top:3390px">
  <span class="icon" style="background:var(--red)"><svg width="22" height="22" viewBox="0 0 24 24"><path d="M5 3l4 4-2 2.5c1.3 3 3.5 5.2 6.5 6.5L16 14l4 4-2.5 3C10 21 3 14 3 5.5z" fill="#fff"/></svg></span>
  <div class="pill-tel"><small>株式会社リペアナビ　工場修繕事業部</small><b>0120-48-3917</b><small>受付時間 平日9:00〜18:00（土日祝休み）</small></div>
</div>
<div class="pill" style="top:3510px">
  <span class="icon" style="background:var(--blue)"><svg width="22" height="18" viewBox="0 0 22 18"><rect x="1" y="1" width="20" height="16" fill="none" stroke="#fff" stroke-width="2"/><path d="M1 2l10 8 10-8" fill="none" stroke="#fff" stroke-width="2"/></svg></span>
  <p style="font-size:17px;font-weight:700"><span style="color:var(--blue)">無料</span>お見積り・お問い合わせ</p>
</div>

<footer class="photo footer"></footer>
<a class="brand" href="#" style="top:3736px;left:192px"><span class="brand-mark"></span><span class="brand-name">工場リペアナビ</span></a>
<p class="abs" style="left:192px;top:3790px;font-family:'Oswald',sans-serif;font-size:30px;font-weight:600">0120-48-3917</p>
<p class="abs" style="left:192px;top:3850px;font-size:11px;line-height:1.8">プライバシーポリシー<br>サイトマップ</p>
<ul class="flinks" style="left:460px"><li>ホーム</li><li>工場リペアナビの特徴</li><li>施工実績</li><li>よくあるご質問</li><li>お打ちかわせの流れ</li></ul>
<ul class="flinks" style="left:690px"><li>サービス一覧</li><li>・屋根・防水</li><li>・電設</li><li>・設備</li><li>・内装工事</li><li>・解体工事</li><li>・省エネ・コスト削減</li></ul>
<ul class="flinks" style="left:890px"><li>会社概要</li><li>コラム</li><li>お知らせ</li><li>無料お見積り・お問い合わせ</li><li>カタログダウンロード</li></ul>
<p class="copy">copyright © REPAIR NAVI Co., Ltd. all rights reserved.</p>

</body>
</html>
```